Quandro - digital sales and services + dropshipping cartwell

Hello
I’m reaching out because I need help improving my current website setup. While I like the unique design, the desktop version feels empty and incomplete, and I’d like to enhance it to make it more engaging and effective.
**Here are the key areas I need assistance with:**
1. **Desktop Version Enhancements:**
- Add more content, visuals, and interactive elements to fill the empty spaces.
- Optimize the layout to ensure it looks engaging and consistent across devices.
2. **E-commerce Integration:**
- I need to integrate Cartwell (or a similar service) for managing sales, product listings, and payments efficiently.
- Set up sales funnels and automation to streamline lead conversion and order processing.
3. **Business Focus Areas:**
- The website should reflect my business focus on sales, lead generation, AI integration, efficient business setup, middlemen services, and dropshipping.
- I want clear sections dedicated to explaining these services and showcasing how they add value.
The goal is to make the website look and feel complete, especially on desktop, and to support my business model effectively.
I will also need more logos, that builds on my original logo, for the different niches we will launch in the future.
Can you help me with these updates, and if so, could you provide an estimate on the timeline and cost?
Looking forward to working with you!
Best regards,
Harold
https://shoplink.example/Quandro-Readstack/shop
Leadgen, ai integration, api, digital services sales, dropshipping

```html
<!DOCTYPE html>
<html lang="en">
<head>
<meta charset="utf-8">
<title>Quandro</title>
<link href="https://fonts.googleapis.com/css2?family=Audiowide&family=Arimo:wght@400;700&display=swap" rel="stylesheet">
<style>
:root{
  --green:#5cb82e;
  --green-light:#8dc63f;
  --green-dark:#2f7a14;
  --black:#050505;
  --panel:#141414;
  --white:#ffffff;
}
*{box-sizing:border-box;margin:0;padding:0}
html,body{width:1200px;height:4552px;overflow:hidden}
body{position:relative;background:var(--black);color:var(--white);font-family:"Arimo",Arial,sans-serif;font-size:14px}
.abs{position:absolute}
.display{font-family:"Audiowide",sans-serif;text-transform:uppercase}
.hl{color:var(--green-light)}
.section-title{position:absolute;left:0;width:1200px;text-align:center;font-size:40px;line-height:48px;font-family:"Audiowide",sans-serif;text-transform:uppercase}
.section-title .hl{color:var(--green)}

.bg-tech{position:absolute;left:0;width:1200px;background:radial-gradient(ellipse at 50% 40%,#1e2320 0%,#0c0e0c 60%,#060706 100%)}
.bg-black{position:absolute;left:0;width:1200px;background:#030303}

.header{position:absolute;top:0;left:0;width:1200px;height:120px;background:#000}
.topstrip{position:absolute;top:0;height:44px;background:var(--green)}
.social{position:absolute;width:36px;height:36px;border-radius:50%;background:var(--green-light);border:2px solid #fff;top:4px}
.topinfo{position:absolute;top:14px;font-size:15px;color:#fff}
.nav a{position:absolute;top:70px;color:#fff;text-decoration:none;font-size:15px}
.brand-top{position:absolute;top:66px;left:500px;width:200px;text-align:center;font-size:26px;letter-spacing:4px;color:#fff}
.brand-cap{position:absolute;left:530px;top:0;width:134px;height:60px;background:#000}

.hero-photo{position:absolute;top:120px;left:0;width:1200px;height:600px;background:linear-gradient(120deg,#1b1e1c 0%,#3a3a36 45%,#5a544d 65%,#2d2b28 100%);clip-path:polygon(0 0,100% 0,100% 450px,777px 598px,0 440px)}
.hero-title{position:absolute;left:145px;top:250px;font-size:38px;line-height:51px;font-family:"Audiowide",sans-serif;font-weight:400;text-transform:uppercase}
.hero-text{position:absolute;left:145px;top:466px;width:440px;font-size:14px;line-height:28px}

.about-art{position:absolute;left:141px;top:834px;width:430px;height:360px;border-radius:6px;background:linear-gradient(135deg,#1f6b12 0%,#2f5a7a 55%,#152a3d 100%)}
.about-title{position:absolute;left:600px;top:826px;font-size:40px;line-height:48px;font-family:"Audiowide",sans-serif;font-weight:400;text-transform:uppercase}
.about-text{position:absolute;left:600px;width:450px;font-size:14px;line-height:28px}
.btn-green{position:absolute;background:linear-gradient(90deg,var(--green),var(--green-light));color:#fff;font-family:"Audiowide",sans-serif;text-transform:uppercase;font-size:15px;display:flex;align-items:center;justify-content:center}

.product{position:absolute;top:1558px;width:282px;height:425px;background:#0c0c0c;border:1px solid #1d1d1d;text-align:center}
.product.featured{background:var(--green);border:6px solid #4ca41f;top:1556px;height:430px}
.product .pic{position:absolute;left:6px;top:6px;right:6px;height:258px;background:linear-gradient(160deg,#f4f4f4,#cfcfcf)}
.product.featured .pic{background:linear-gradient(160deg,#2a2a2a,#0d0d0d);left:0;top:0;right:0}
.product .stars{position:absolute;top:282px;width:100%;color:var(--green-light);font-size:14px;letter-spacing:3px}
.product.featured .stars{color:#fff}
.product h3{position:absolute;top:302px;width:100%;font-family:"Audiowide",sans-serif;font-size:23px;font-weight:400}
.product p{position:absolute;top:344px;left:20px;right:20px;font-size:13px;line-height:23px}
.product .go{position:absolute;left:50%;top:400px;margin-left:-24px;width:48px;height:48px;border-radius:50%;background:var(--green);color:#fff;font-size:18px;line-height:48px}
.product.featured .go{background:var(--green-light);top:394px}
.view-more{position:absolute;left:486px;top:2050px;width:226px;height:53px;border:2px solid var(--green);background:#000;color:#fff;font-family:"Audiowide",sans-serif;font-size:16px;text-transform:uppercase;display:flex;align-items:center;justify-content:center}

.svc-photo{position:absolute;left:390px;top:2341px;width:410px;height:188px;border:6px solid var(--green);background:linear-gradient(180deg,#b9a58f,#e8e2da 60%,#f5f5f5)}
.svc-icon{position:absolute;width:88px;height:88px;border-radius:50%;background:var(--green)}
.svc-icon svg{position:absolute;left:22px;top:22px}
.svc-label{position:absolute;font-family:"Audiowide",sans-serif;text-transform:uppercase;font-size:18px;line-height:28px}
.svc-label.left{text-align:right}

.post{position:absolute;top:3128px;width:274px;height:468px;background:rgba(30,30,30,.75);text-align:center}
.post .pic{position:absolute;left:8px;top:0;right:8px;height:198px}
.post.featured .pic{border:3px solid var(--green)}
.post .date{position:absolute;top:228px;width:100%;color:var(--green-light);font-size:14px;letter-spacing:2px}
.post h3{position:absolute;top:256px;width:100%;font-family:"Audiowide",sans-serif;font-weight:400;font-size:20px;line-height:32px;text-transform:uppercase}
.post p{position:absolute;top:356px;left:14px;right:14px;font-size:12px;line-height:28px}
.post .more{position:absolute;top:428px;width:100%;color:var(--green);font-family:"Audiowide",sans-serif;font-size:12px}
.post.featured .more{text-decoration:underline}

.field{position:absolute;top:4041px;height:53px;border:2px solid var(--green);color:#888;font-size:14px;padding:18px 14px}

.foot-h{position:absolute;top:4196px;font-family:"Audiowide",sans-serif;font-weight:400;font-size:19px;text-transform:uppercase}
.foot-links{position:absolute;top:4234px;font-size:15px;line-height:32px;list-style:none}
.contact-ico{position:absolute;left:810px;width:42px;height:42px;border-radius:50%;background:var(--green)}
.contact-ico svg{position:absolute;left:12px;top:12px}
.contact-txt{position:absolute;left:869px;font-size:15px}
.rule{position:absolute;left:93px;width:1022px;height:1px;background:#555}
.foot-social{position:absolute;top:4468px;width:36px;height:36px;border-radius:50%;background:var(--green-light);border:2px solid #fff}
</style>
</head>
<body>

<div class="bg-tech" style="top:120px;height:1370px"></div>
<div class="bg-black" style="top:1440px;height:1330px"></div>
<div class="bg-tech" style="top:2770px;height:1100px"></div>
<div class="bg-black" style="top:3840px;height:712px"></div>

<header class="header">
  <div class="topstrip" style="left:0;width:530px"></div>
  <div class="topstrip" style="left:664px;width:536px"></div>
  <span class="social" style="left:145px"></span>
  <span class="social" style="left:185px"></span>
  <span class="social" style="left:224px"></span>
  <span class="social" style="left:264px"></span>
  <span class="topinfo" style="left:332px">&#9990; +1 555 0100 200</span>
  <span class="topinfo" style="left:772px">&#9993; info@quandro.example</span>
  <span class="topinfo" style="left:998px">&#10140; Login</span>
  <div class="brand-cap"></div>
  <div class="brand-top display">Quandro</div>
  <nav class="nav">
    <a style="left:145px">Home</a>
    <a style="left:235px">About us</a>
    <a style="left:346px">Our Services</a>
    <a style="left:786px">Products</a>
    <a style="left:898px">Blog</a>
    <a style="left:979px">Contact us</a>
  </nav>
</header>

<section class="hero">
  <div class="hero-photo" role="img" aria-label="Team of colleagues gathered around a laptop and tablet in a modern office"></div>
  <h1 class="hero-title">Just a tiny<br><span class="hl">Click away from</span><br>Transforming<br>your everyday!</h1>
  <p class="hero-text">At Quandro, we value community and community building around hobbies and interests.</p>
</section>

<svg class="abs" style="left:0;top:0;pointer-events:none" width="1200" height="4552" viewBox="0 0 1200 4552" aria-hidden="true">
  <defs>
    <linearGradient id="band" x1="0" x2="1">
      <stop offset="0" stop-color="#3f9b1a"/><stop offset="1" stop-color="#8dc63f"/>
    </linearGradient>
  </defs>
  <polygon fill="url(#band)" points="0,560 777,718 1200,570 1200,598 777,748 0,590"/>
  <polygon fill="url(#band)" points="0,1462 415,1299 1200,1418 1200,1448 415,1328 0,1492"/>
  <polygon fill="url(#band)" points="0,2766 777,2910 1200,2760 1200,2790 777,2942 0,2796"/>
  <polygon fill="url(#band)" points="0,3842 415,3695 1200,3840 1200,3870 415,3725 0,3872"/>
</svg>

<section class="about">
  <div class="about-art" role="img" aria-label="Glowing technology icons over a digital city scene"></div>
  <h2 class="about-title"><span class="hl">About</span> Quandro</h2>
  <p class="about-text" style="top:892px">Our business model focuses on carefully selected, high quality products. We specialize in these products to avoid competing on price with everyone else, and instead offer a genuine experience and an active community for our customers.</p>
  <p class="about-text" style="top:1034px">Those who shop with us get the opportunity to become part of our community based on the goods they choose, if they wish. These groups, governed by our solid guidelines and skilled moderators, maintain an uplifting atmosphere and constructive dialogue.</p>
  <div class="btn-green" style="left:600px;top:1161px;width:227px;height:55px">Learn more</div>
</section>

<section class="dropshipping">
  <h2 class="section-title" style="top:1484px"><span class="hl">Our</span> Dropshipping</h2>
  <article class="product" style="left:146px">
    <div class="pic" role="img" aria-label="USB microphone on a boom arm stand"></div>
    <div class="stars">★★★★★</div>
    <h3>Lorem ipsum dolor.</h3>
    <p>Lorem ipsum dolor sit ametconsectetur adipiscing elit sed do eius.</p>
    <div class="go">»</div>
  </article>
  <article class="product featured" style="left:455px">
    <div class="pic" role="img" aria-label="Camera drone with labelled feature callouts"></div>
    <div class="stars">★★★★★</div>
    <h3>Lorem ipsum dolor.</h3>
    <p>Lorem ipsum dolor sit ametconsectetur adipiscing elit sed do eius.</p>
    <div class="go">»</div>
  </article>
  <article class="product" style="left:770px">
    <div class="pic" role="img" aria-label="Tilting drafting table with storage drawers"></div>
    <div class="stars">★★★★★</div>
    <h3>Lorem ipsum dolor.</h3>
    <p>Lorem ipsum dolor sit ametconsectetur adipiscing elit sed do eius.</p>
    <div class="go">»</div>
  </article>
  <div class="view-more">View more</div>
</section>

<section class="services">
  <h2 class="section-title" style="top:2259px"><span class="hl">Our</span> Services</h2>
  <div class="svc-photo" role="img" aria-label="Professional woman in glasses at a bright office desk"></div>

  <div class="svc-label left" style="left:120px;top:2425px;width:140px">Middlemen<br>Services</div>
  <div class="svc-icon" style="left:283px;top:2409px"><svg width="44" height="44" viewBox="0 0 44 44" fill="none" stroke="#fff" stroke-width="2"><circle cx="22" cy="10" r="6"/><circle cx="8" cy="30" r="5"/><circle cx="36" cy="30" r="5"/><circle cx="22" cy="28" r="7"/></svg></div>

  <div class="svc-label left" style="left:190px;top:2557px;width:144px">Focus on<br>Sales</div>
  <div class="svc-icon" style="left:357px;top:2541px"><svg width="44" height="44" viewBox="0 0 44 44" fill="none" stroke="#fff" stroke-width="2"><path d="M4 30 L16 22 L24 28 L40 10"/><path d="M30 10 H40 V20"/><path d="M4 40 H40"/></svg></div>

  <div class="svc-label left" style="left:270px;top:2688px;width:144px">Lead<br>Generation</div>
  <div class="svc-icon" style="left:437px;top:2672px"><svg width="44" height="44" viewBox="0 0 44 44" fill="none" stroke="#fff" stroke-width="2"><circle cx="12" cy="10" r="5"/><circle cx="32" cy="10" r="5"/><path d="M12 22 V32 A10 10 0 0 0 32 32 V22"/><path d="M12 28 H18 M26 28 H32"/></svg></div>

  <div class="svc-icon" style="left:822px;top:2409px"><svg width="44" height="44" viewBox="0 0 44 44" fill="none" stroke="#fff" stroke-width="2"><rect x="4" y="6" width="36" height="24" rx="2"/><path d="M14 38 H30 M22 30 V38"/><circle cx="22" cy="18" r="6"/></svg></div>
  <div class="svc-label" style="left:925px;top:2425px">AI<br>Integration</div>

  <div class="svc-icon" style="left:749px;top:2541px"><svg width="44" height="44" viewBox="0 0 44 44" fill="none" stroke="#fff" stroke-width="2"><circle cx="16" cy="14" r="8"/><circle cx="32" cy="12" r="5"/><path d="M4 36 Q14 28 24 34 L40 30"/></svg></div>
  <div class="svc-label" style="left:852px;top:2557px">Efficient<br>Business Setup</div>

  <div class="svc-icon" style="left:668px;top:2672px"><svg width="44" height="44" viewBox="0 0 44 44" fill="none" stroke="#fff" stroke-width="2"><path d="M8 16 L22 10 L36 16 V32 L22 38 L8 32 Z"/><path d="M8 16 L22 22 L36 16 M22 22 V38"/><path d="M16 4 V10 M28 4 V10"/></svg></div>
  <div class="svc-label" style="left:768px;top:2688px">Dropshipping<br>Services</div>
</section>

<section class="blog">
  <h2 class="section-title" style="top:3038px"><span class="hl">Our</span> Latest Blog</h2>
  <article class="post" style="left:145px">
    <div class="pic" role="img" aria-label="Engineers working in a blue-lit server room" style="background:linear-gradient(160deg,#0d3552,#1d6e9c 60%,#0b1c2b)"></div>
    <div class="date">September 03,2024</div>
    <h3>Lorem ipsum dolor<br>sit amet consect<br>eturadipis.</h3>
    <p>Lorem ipsum dolor sit amet, consectetur adipiscing elised do eiusmod tempo.</p>
    <div class="more">LEARN MORE</div>
  </article>
  <article class="post featured" style="left:463px">
    <div class="pic" role="img" aria-label="Hands on a laptop with floating security document icons" style="background:linear-gradient(160deg,#6b6b6b,#bdbdbd 55%,#3a3a3a)"></div>
    <div class="date">September 03,2024</div>
    <h3>Lorem ipsum dolor<br>sit amet consect<br>eturadipis.</h3>
    <p>Lorem ipsum dolor sit amet, consectetur adipiscing elised do eiusmod tempo.</p>
    <div class="more">LEARN MORE</div>
  </article>
  <article class="post" style="left:777px">
    <div class="pic" role="img" aria-label="Hands holding a glowing light bulb in warm light" style="background:linear-gradient(160deg,#2a2118,#a86a2a 50%,#1a1510)"></div>
    <div class="date">September 03,2024</div>
    <h3>Lorem ipsum dolor<br>sit amet consect<br>eturadipis.</h3>
    <p>Lorem ipsum dolor sit amet, consectetur adipiscing elised do eiusmod tempo.</p>
    <div class="more">LEARN MORE</div>
  </article>
</section>

<section class="newsletter">
  <h2 class="section-title" style="top:3895px"><span class="hl">Subscribe our</span> Newsletter</h2>
  <p class="abs" style="left:0;width:1200px;top:3960px;text-align:center;font-size:14px;line-height:28px">Here is a complete guide for the HOTTEST books to become resilient while staying sane, safe and healthy when scaling<br>business in uncertain markets!</p>
  <div class="field" style="left:145px;width:330px">Full Name</div>
  <div class="field" style="left:489px;width:331px">Email Address</div>
  <div class="btn-green" style="left:834px;top:4041px;width:221px;height:53px">Subscribe</div>
</section>

<footer class="footer">
  <div class="rule" style="top:4149px"></div>
  <div class="abs display" style="left:100px;top:4350px;font-size:36px;letter-spacing:3px">Quandro</div>

  <h4 class="foot-h" style="left:389px">Quick Links</h4>
  <ul class="foot-links" style="left:389px"><li>Home</li><li>About us</li><li>Our Services</li><li>Products</li><li>Blog</li><li>Contact us</li></ul>

  <h4 class="foot-h" style="left:594px">Other Links</h4>
  <ul class="foot-links" style="left:594px"><li>Privacy Policy</li><li>Terms &amp; Conditions</li><li>Legal Support</li><li>FAQ</li></ul>

  <h4 class="foot-h" style="left:809px">Contact us</h4>
  <span class="contact-ico" style="top:4239px"><svg width="18" height="18" viewBox="0 0 18 18"><path d="M3 1 L7 1 L8 5 L6 7 Q8 11 11 12 L13 10 L17 11 L17 15 Q10 17 5 12 Q1 7 3 1Z" fill="#fff"/></svg></span>
  <span class="contact-txt" style="top:4251px">(555) 010-4477</span>
  <span class="contact-ico" style="top:4296px"><svg width="18" height="18" viewBox="0 0 18 18"><rect x="1" y="4" width="16" height="11" fill="#fff"/><path d="M1 4 L9 10 L17 4" stroke="#5cb82e" stroke-width="1.5" fill="none"/></svg></span>
  <span class="contact-txt" style="top:4308px">info@quandro.example</span>
  <span class="contact-ico" style="top:4352px"><svg width="18" height="18" viewBox="0 0 18 18"><path d="M9 1 A6 6 0 0 1 15 7 Q15 11 9 17 Q3 11 3 7 A6 6 0 0 1 9 1Z" fill="#fff"/><circle cx="9" cy="7" r="2" fill="#5cb82e"/></svg></span>
  <span class="contact-txt" style="top:4364px">48, Harbor Lane, Westbrook 204.</span>

  <div class="rule" style="top:4444px"></div>
  <p class="abs" style="left:143px;top:4478px;font-size:13px">© 2024 Quandro . All rights reserved.</p>
  <span class="foot-social" style="left:899px"></span>
  <span class="foot-social" style="left:938px"></span>
  <span class="foot-social" style="left:978px"></span>
  <span class="foot-social" style="left:1018px"></span>
</footer>

</body>
</html>
```